Looking for attractive banner design (print banner)

I am looking to redesign a banner to be more attractive and professional. This will be a print banner, 24" x 36" vertical. I am attaching the original concept to reference. High resolution file for print required. fading or blurring the background, attractive fonts, gradient highlight for text boxes, etc.

```html
<!DOCTYPE html>
<html lang="en">
<head>
<meta charset="utf-8">
<title>Essential Oils for the Horse &amp; Rider</title>
<link rel="stylesheet" href="https://fonts.googleapis.com/css2?family=Dancing+Script:wght@700&family=Oswald:wght@300;400;600;700&display=swap">
<style>
  :root {
    --page-bg: #4e4e4e;
    --sky-top: #bcd2e8;
    --sky-mid: #d3e0ec;
    --sky-low: #c6d6e4;
    --field-green: #6f8a3c;
    --field-dark: #4a6a2c;
    --brand-blue: #0b3aa8;
    --deep-blue: #0a2b86;
    --body-text: #1f2530;
    --divider: rgba(30, 50, 90, 0.18);
    --disclaimer: #f1f1ee;
  }
  * { margin: 0; padding: 0; box-sizing: border-box; }
  html, body { width: 1200px; height: 900px; overflow: hidden; background: var(--page-bg); }
  .banner {
    position: absolute; left: 300px; top: 0; width: 600px; height: 900px; overflow: hidden;
    background: linear-gradient(180deg, var(--sky-top) 0%, var(--sky-mid) 45%, var(--sky-low) 70%);
    font-family: 'Oswald', sans-serif;
  }
  .scene-photo {
    position: absolute; left: 0; top: 455px; width: 600px; height: 435px;
    background: linear-gradient(180deg,
      rgba(198, 214, 228, 0) 0%,
      rgba(178, 198, 218, 0.6) 40%,
      #a9bccd 62%,
      var(--field-dark) 72%,
      var(--field-green) 86%,
      #8a9a50 100%);
  }
  .title-script {
    position: absolute; left: 0; width: 600px; top: 38px; text-align: center;
    font-family: 'Dancing Script', cursive; font-weight: 700; font-size: 76px;
    color: var(--brand-blue); line-height: 1;
  }
  .title-main {
    position: absolute; left: 103px; top: 115px; transform-origin: 0 0; transform: scaleX(0.88);
    font-weight: 700; font-size: 76px; line-height: 1; color: var(--brand-blue); letter-spacing: -1px;
    white-space: nowrap;
  }
  .title-prefix {
    position: absolute; left: 86px; top: 186px; transform-origin: 0 0; transform: rotate(-90deg);
    font-weight: 600; font-size: 15px; line-height: 1; color: var(--brand-blue); letter-spacing: 0.5px;
    white-space: nowrap;
  }
  .rule-dotted { position: absolute; left: 118px; top: 233px; width: 366px; border-top: 3px dotted var(--brand-blue); }
  .col-divider { position: absolute; top: 273px; height: 186px; border-left: 1px solid var(--divider); }
  .oil-group { position: absolute; width: 172px; }
  .oil-group.right { text-align: right; }
  .oil-group h3 { font-weight: 600; font-size: 13.5px; color: var(--brand-blue); line-height: 1.15; letter-spacing: -0.2px; }
  .oil-group p { font-weight: 300; font-size: 12.5px; color: var(--body-text); line-height: 16px; letter-spacing: -0.2px; }
  .disclaimer {
    position: absolute; left: 0; width: 600px; top: 862px; text-align: center;
    font-weight: 600; font-size: 14px; letter-spacing: 2.3px; color: var(--disclaimer);
    text-shadow: 0 1px 2px rgba(0,0,0,0.5);
  }
  .base-band { position: absolute; left: 0; bottom: 0; width: 600px; height: 10px; background: var(--deep-blue); }
</style>
</head>
<body>
<main class="banner">
  <div class="scene-photo" role="img" aria-label="Photo of a young rider in white shirt and helmet on a chestnut horse, trotting in a green field with trees and a fence under a cloudy blue sky"></div>

  <h1>
    <span class="title-script">Essential Oils</span>
    <span class="title-prefix">FOR THE</span>
    <span class="title-main">HORSE &amp; RIDER</span>
  </h1>
  <div class="rule-dotted"></div>

  <div class="col-divider" style="left:228px"></div>
  <div class="col-divider" style="left:426px"></div>

  <section class="oil-group" style="left:53px;top:272px"><h3>BRAIN</h3><p>Frankincense, Mind Spark,<br>Clear Focus, Cedarwood</p></section>
  <section class="oil-group" style="left:53px;top:335px"><h3>SKIN &amp; HAIR</h3><p>Cedarwood, Lavender, Geranium,<br>Frankincense, Myrrh</p></section>
  <section class="oil-group" style="left:53px;top:399px"><h3>EARS</h3><p>Helichrysum, Fresh Air,<br>Tea Tree, Juniper</p></section>
  <section class="oil-group" style="left:53px;top:462px"><h3>LUNGS</h3><p>B.R., Night Breath, Eucalyptus (all),<br>Guardian, Tea Tree, Azure Gold</p></section>
  <section class="oil-group" style="left:53px;top:526px"><h3>MUSCLES</h3><p>Muscle Ease, Deep Calm,<br>Marjoram, Cypress, Peppermint,<br>Grand Fir</p></section>
  <section class="oil-group" style="left:53px;top:605px"><h3>IMMUNE SUPPORT</h3><p>Guardian, Oregano, Ocotea,<br>Evergreen, Lemon, Peppermint,<br>Cinnamon Bark, Rosemary</p></section>

  <section class="oil-group" style="left:247px;top:273px"><h3>TENDONS &amp; LIGAMENTS</h3><p>Palo Santo, Lemongrass, Rosemary,<br>Peppermint</p></section>
  <section class="oil-group" style="left:247px;top:336px"><h3>HOOF (HORSE)</h3><p>Guardian, Tea Tree, Oregano,<br>Frankincense</p></section>
  <section class="oil-group" style="left:247px;top:400px"><h3>EMOTIONAL SUPPORT</h3><p>Courage, Willow, Full Bloom, Delight,<br>Lemon</p></section>

  <section class="oil-group right" style="left:403px;top:273px"><h3>EYES</h3><p>Frankincense, Sandalwood,<br>Carrot Seed, Lemongrass</p></section>
  <section class="oil-group right" style="left:403px;top:336px"><h3>MOUTH</h3><p>Clove, Ocotea, Tea Tree,<br>Wintergreen, Guardian</p></section>
  <section class="oil-group right" style="left:403px;top:400px"><h3>HEART</h3><p>Orange, Ylang Ylang, Cypress,<br>Helichrysum, Palmarosa</p></section>
  <section class="oil-group right" style="left:403px;top:463px"><h3>DIGESTION</h3><p>Gut Ease, Calm Tummy, Ginger,<br>Fennel, Peppermint</p></section>
  <section class="oil-group right" style="left:403px;top:527px"><h3>HORMONAL BALANCE</h3><p>Clary Sage, Moon Cycle,<br>Endo Calm, Myrtle, Azure Gold</p></section>
  <section class="oil-group right" style="left:403px;top:591px"><h3>BONES AND JOINTS</h3><p>Pain Fade, Helichrysum,<br>Wintergreen, Cool Blue, Courage</p></section>
  <section class="oil-group right" style="left:403px;top:654px"><h3>FEET (RIDER)</h3><p>Rooted, Courage, Guardian,<br>Fresh Air, Oregano</p></section>

  <p class="disclaimer">DISCLAIMER: NOT EVALUATED BY THE FDA, NOT MEDICAL ADVICE</p>
  <div class="base-band"></div>
</main>
</body>
</html>
```